Business Card design for Property Developer

We need a business card design for a Melbourne based Property Developer called "Kestrelmoor Holdings Pty Ltd".

We subdivide land and onsell to builders etc.

We already have a company logo, which is attached. Also I have attached the layout requirements from the printer. We would like a 2-sided design with one side displaying our logo by itself and the other with the required info, such as name, address, tel no., email, abn etc. The card will need to be used by 4 members of staff so name and contact details should be interchangable.
Updates

If possible, can you please write "name' "job position" "phone" "email" "address" on the card but leave them so I can add the details at a later time. Thank you. Also I plan on printing with UV spot printing as a background on the card. Keep this is mind when designing.

Thanks again.

Hello designers, please do not include pics of houses, house plansĀ or construction machinery etc as we really do not like the way it looks. Thank you.

Target Market(s)

Real Estate Agents, Land Owners, Local Council Departments, Govt Bodies, other Developers etc.

Industry/Entity Type

Business

Requirements
Must have
• 2-sided design with one side displaying our logo by itself and the other with the required info, such as name, address, tel no., email, abn etc.

```html
<!DOCTYPE html>
<html lang="en">
<head>
<meta charset="utf-8">
<title>Kestrelmoor Holdings – Business Card</title>
<link rel="stylesheet" href="https://fonts.googleapis.com/css2?family=EB+Garamond:wght@400;600&display=swap">
<style>
  :root {
    --stage: #000000;
    --card: #ffffff;
    --ink: #2b2b2b;
    --brand: #2a3f8f;
    --brand-ring: #4f6fc0;
    --serif: "EB Garamond", Georgia, serif;
  }
  html, body {
    margin: 0;
    padding: 0;
    width: 1200px;
    height: 900px;
    overflow: hidden;
    background: var(--stage);
  }
  .stage {
    position: relative;
    width: 1200px;
    height: 900px;
    font-family: var(--serif);
  }
  .card {
    position: absolute;
    background: var(--card);
    overflow: hidden;
  }
  .card--front { left: 36px; top: 46px; width: 654px; height: 353px; }
  .card--back  { left: 470px; top: 476px; width: 656px; height: 352px; }

  /* brand lockup */
  .brand {
    position: absolute;
    display: flex;
    flex-direction: column;
    align-items: center;
    color: var(--brand);
  }
  .brand__disc { display: block; }
  .brand__name {
    font-family: var(--serif);
    font-weight: 600;
    text-transform: uppercase;
    color: var(--brand);
    text-align: center;
    line-height: 1;
    letter-spacing: 0.06em;
  }
  .card--front .brand { left: 0; right: 0; top: 48px; }
  .card--front .brand__disc { width: 170px; height: 170px; margin-bottom: 26px; }
  .card--front .brand__name { font-size: 46px; }

  .card--back .brand { left: 460px; width: 176px; top: 28px; }
  .card--back .brand__disc { width: 66px; height: 66px; margin-bottom: 12px; }
  .card--back .brand__name { font-size: 17px; line-height: 1.1; }

  /* contact details */
  .person {
    position: absolute;
    left: 93px;
    top: 48px;
    color: var(--ink);
  }
  .person__name {
    margin: 0;
    font-weight: 400;
    font-size: 30px;
    line-height: 1;
  }
  .person__name .initial { font-size: 50px; }
  .person__role {
    margin: 0 0 0 22px;
    font-size: 19px;
    line-height: 1;
  }
  .person__email {
    margin: 4px 0 0 22px;
    font-size: 15px;
    line-height: 1;
  }
  .address {
    position: absolute;
    left: 259px;
    width: 200px;
    top: 144px;
    text-align: center;
    font-style: normal;
    font-size: 17px;
    line-height: 19.5px;
    color: var(--ink);
  }
  .lines {
    position: absolute;
    right: 34px;
    top: 284px;
    text-align: right;
    font-size: 15px;
    line-height: 19px;
    color: var(--ink);
    margin: 0;
  }
</style>
</head>
<body>
<main class="stage">

  <section class="card card--front" aria-label="Card front">
    <div class="brand">
      <svg class="brand__disc" viewBox="0 0 100 100" aria-hidden="true">
        <circle cx="50" cy="50" r="44" fill="none" stroke="var(--brand-ring)" stroke-width="8"/>
      </svg>
      <span class="brand__name">Kestrelmoor Holdings</span>
    </div>
  </section>

  <section class="card card--back" aria-label="Card back">
    <div class="person">
      <h1 class="person__name"><span class="initial">J</span>ohn <span class="initial">D</span>oe</h1>
      <p class="person__role">Job Position</p>
      <p class="person__email">JohnDoe@kestrelmoor.au</p>
    </div>

    <address class="address">
      1234 Poplar Street<br>
      America, USA<br>
      12345-1234
    </address>

    <p class="lines">
      Tel: 1-123-456-7890 Ex. 123<br>
      Fax: 1-123-456-7890 Ex. 123
    </p>

    <div class="brand">
      <svg class="brand__disc" viewBox="0 0 100 100" aria-hidden="true">
        <circle cx="50" cy="50" r="42" fill="none" stroke="var(--brand-ring)" stroke-width="10"/>
      </svg>
      <span class="brand__name">Kestrelmoor Holdings</span>
    </div>
  </section>

</main>
</body>
</html>
```